Electronic Letterhead for The Quillmere Group, LLC

I would like to have an electronic letterhead layout using Word for first and second page letterhead using my previously designed logo. The logo was successfully designed by a designer for the Pixel Bazaar. I would like to only use the "C" portion of the logo on the second page. I would like the designer that designed my logo to be included in the designers that participate in this competition.

Target Market(s)

My clients are typically governmental entities or financial entities

Industry/Entity Type

Electronic

Font styles to use
Sans Serif

Requirements
Must have
• Utilize existing logo
Nice to have
• Fist and second page letterhead design in electronic format (Word)

```html
<!DOCTYPE html>
<html lang="en">
<head>
<meta charset="utf-8">
<title>The Quillmere Group, LLC — Letterhead</title>
<link href="https://fonts.googleapis.com/css2?family=Libre+Baskerville&family=Roboto:wght@400;700&display=swap" rel="stylesheet">
<style>
  :root {
    --backdrop-light: #7c7c7c;
    --backdrop-dark: #4e4e4e;
    --paper: #ffffff;
    --navy: #0d3a7e;
    --band-grey: #555555;
    --watermark: #e0e6ef;
    --ink: #1f2f4f;
    --rule: #9a9a9a;
  }
  * { margin: 0; padding: 0; box-sizing: border-box; }
  html, body { width: 1200px; height: 1000px; overflow: hidden; }
  body {
    position: relative;
    background: linear-gradient(135deg, var(--backdrop-light) 0%, #656565 50%, var(--backdrop-dark) 100%);
    font-family: "Roboto", Arial, sans-serif;
  }
  .sheet {
    position: absolute;
    top: 91px;
    width: 545px;
    height: 773px;
    background: var(--paper);
    box-shadow: 3px 4px 6px rgba(0,0,0,0.45);
    overflow: hidden;
  }
  .sheet--first { left: 37px; }
  .sheet--second { left: 614px; height: 771px; }
  .top-band { position: absolute; top: 0; left: 0; width: 545px; height: 30px; }
  .bottom-band { position: absolute; bottom: 0; left: 0; width: 545px; height: 16px; }
  .watermark {
    position: absolute;
    left: 158px; top: 334px;
    width: 232px; height: 232px;
    border-radius: 50%;
    background: var(--watermark);
  }
  .brand {
    position: absolute;
    left: 44px; top: 37px;
    display: flex; align-items: center;
  }
  .brand__dot {
    width: 44px; height: 44px; border-radius: 50%;
    background: var(--navy);
  }
  .brand__rule { width: 1px; height: 46px; background: var(--rule); margin: 0 4px 0 5px; }
  .brand__name {
    font-family: "Libre Baskerville", Georgia, serif;
    color: var(--navy);
    text-transform: uppercase;
    line-height: 1.25;
  }
  .brand__the { display: block; font-size: 8px; }
  .brand__main { display: block; font-size: 13.5px; }
  .brand__group { display: block; font-size: 11px; }
  .brand__group small, .running-title small { font-size: 0.7em; }
  .running-title {
    position: absolute;
    top: 9px; right: 32px;
    font-family: "Libre Baskerville", Georgia, serif;
    color: #ffffff;
    font-size: 13px;
    letter-spacing: 0.2px;
    text-transform: uppercase;
    white-space: nowrap;
  }
  .running-title .small-word { font-size: 9px; }
  .signatory {
    position: absolute; left: 35px; top: 728px;
    color: var(--navy);
  }
  .signatory__name { font-size: 10.5px; font-weight: 700; letter-spacing: 0.3px; }
  .signatory__phone { font-size: 7.5px; font-weight: 700; }
  .contact-rule { position: absolute; left: 113px; top: 723px; width: 1px; height: 31px; background: var(--rule); }
  .contact-list {
    position: absolute; left: 122px; top: 723px;
    list-style: none;
    font-size: 7.5px; color: var(--ink);
  }
  .contact-list li { display: flex; align-items: center; height: 10px; white-space: nowrap; }
  .contact-list svg { width: 8px; height: 8px; margin-right: 4px; flex: none; }
</style>
</head>
<body>

<section class="sheet sheet--first" aria-label="First page letterhead">
  <svg class="top-band" viewBox="0 0 545 30" aria-hidden="true">
    <path d="M183 0 H545 V23 H225 C205 23 202 0 183 0 Z" fill="var(--band-grey)"/>
  </svg>

  <div class="brand">
    <div class="brand__dot"></div>
    <div class="brand__rule"></div>
    <div class="brand__name">
      <span class="brand__the">The</span>
      <span class="brand__main">Quillmere</span>
      <span class="brand__group">Group, <small>LLC</small></span>
    </div>
  </div>

  <div class="watermark" aria-hidden="true"></div>

  <div class="signatory">
    <div class="signatory__name">R. J. Marlowe</div>
    <div class="signatory__phone">Phone: 0400555019</div>
  </div>
  <div class="contact-rule"></div>
  <ul class="contact-list">
    <li><svg viewBox="0 0 8 8"><rect width="8" height="8" rx="2" fill="var(--navy)"/><path d="M1.5 2.5h5v3h-5z M1.5 2.5l2.5 2 2.5-2" fill="none" stroke="#fff" stroke-width="0.7"/></svg>rjmarlowe@quillmere.example</li>
    <li><svg viewBox="0 0 8 8"><rect width="8" height="8" rx="2" fill="var(--navy)"/><circle cx="4" cy="4" r="2.4" fill="none" stroke="#fff" stroke-width="0.7"/><path d="M1.6 4h4.8" stroke="#fff" stroke-width="0.6"/></svg>www.quillmere.example</li>
    <li><svg viewBox="0 0 8 8"><rect width="8" height="8" rx="2" fill="var(--navy)"/><path d="M4 7 C2 4.5 2 3.5 2 3 A2 2 0 0 1 6 3 C6 3.5 6 4.5 4 7Z" fill="#fff"/></svg>PO Box 4410 Tarrow, NSW, 2600</li>
  </ul>

  <svg class="bottom-band" viewBox="0 0 545 16" aria-hidden="true">
    <path d="M350 2 H545 V16 H372 C362 16 360 2 350 2 Z" fill="var(--band-grey)"/>
    <path d="M0 2 H325 C345 2 350 16 358 16 H0 Z" fill="var(--navy)"/>
  </svg>
</section>

<section class="sheet sheet--second" aria-label="Second page letterhead">
  <svg class="top-band" viewBox="0 0 545 30" aria-hidden="true">
    <path d="M241 0 H545 V30 H286 C266 30 262 0 241 0 Z" fill="var(--band-grey)"/>
  </svg>
  <div class="running-title"><span class="small-word">The</span> Quillmere Group, <small>LLC</small></div>

  <div class="watermark" aria-hidden="true"></div>

  <svg class="bottom-band" viewBox="0 0 545 16" aria-hidden="true">
    <path d="M350 2 H545 V16 H372 C362 16 360 2 350 2 Z" fill="var(--band-grey)"/>
    <path d="M0 2 H325 C345 2 350 16 358 16 H0 Z" fill="var(--navy)"/>
  </svg>
</section>

</body>
</html>
```